Some great artwork for my new hip-hop album!!!

Hey! I need a CD cover done. The title is " Quiet Harbours " and I want to have a heart as the background, with the title inside of the heart in different colours for every letter. I am open to ideas and different interpretations from you artists but I really need the phrase "Quiet Harbours" to be the biggest part. If you can find a totally different idea that seems to fit that better, go for it! I am excited to see what you come up with and thank you!
Target Market(s)
Hip Hop Listeners/Everyone!
Colors
Designer to choose colors to be used in the design.
Requirements
Must have
- The needs in the description, that being a heart as the background and the words Quiet Harbours written inside the heart with each letter a different colour. Anything else you want to add is up to you if it looks great!

Nice to have
- Just want a great eye catching album cover to get people to listen to my music, and I need YOUR help!

```html
<!DOCTYPE html>
<html lang="en">
<head>
<meta charset="UTF-8">
<title>Quiet Harbours — Album Cover</title>
<link rel="stylesheet" href="https://fonts.googleapis.com/css2?family=Archivo+Black&display=swap">
<style>
  :root {
    --paper: #f6f4ec;
    --mist: #eef0e6;
    --leaf-yellow: #f3d64a;
    --leaf-gold: #e9b93a;
    --leaf-orange: #e58a3c;
    --water-teal: #a9d3c4;
    --heart-top: #1f5f8b;
    --heart-mid: #2a9d8f;
    --heart-low: #e76f51;
    --c1: #1d3557;
    --c2: #e63946;
    --c3: #2a9d8f;
    --c4: #f4a261;
    --c5: #457b9d;
    --c6: #d62f7a;
    --c7: #264653;
    --c8: #e76f51;
    --c9: #3a86ff;
    --c10: #8a5a00;
    --c11: #06837a;
    --c12: #b5179e;
    --c13: #355070;
  }
  html, body {
    margin: 0;
    padding: 0;
    width: 1200px;
    height: 1200px;
    overflow: hidden;
    background: var(--paper);
  }
  .cover {
    position: relative;
    width: 1200px;
    height: 1200px;
    overflow: hidden;
  }
  .cover__scenery {
    position: absolute;
    inset: 0;
    background:
      radial-gradient(ellipse 48% 40% at 50% 50%, var(--paper) 0%, rgba(246,244,236,0.92) 55%, rgba(246,244,236,0) 100%),
      radial-gradient(ellipse 30% 25% at 12% 14%, var(--leaf-gold) 0%, rgba(233,185,58,0) 100%),
      radial-gradient(ellipse 22% 20% at 95% 32%, var(--leaf-orange) 0%, rgba(229,138,60,0) 100%),
      radial-gradient(ellipse 20% 22% at 4% 72%, var(--leaf-orange) 0%, rgba(229,138,60,0) 100%),
      radial-gradient(ellipse 30% 22% at 85% 88%, var(--leaf-yellow) 0%, rgba(243,214,74,0) 100%),
      linear-gradient(180deg, #f3e7a8 0%, var(--mist) 30%, var(--water-teal) 52%, var(--mist) 70%, #f2e49a 100%);
  }
  .cover__heart {
    position: absolute;
    inset: 0;
  }
  .cover__title {
    position: absolute;
    left: 0;
    right: 0;
    top: 508px;
    margin: 0;
    text-align: center;
    font-family: "Archivo Black", "Arial Black", sans-serif;
    font-weight: 400;
    font-size: 52px;
    line-height: 1;
    letter-spacing: 3px;
    text-transform: uppercase;
    white-space: nowrap;
  }
  .l1 { color: var(--c1); }
  .l2 { color: var(--c2); }
  .l3 { color: var(--c3); }
  .l4 { color: var(--c4); }
  .l5 { color: var(--c5); }
  .l6 { color: var(--c6); }
  .l7 { color: var(--c7); }
  .l8 { color: var(--c8); }
  .l9 { color: var(--c9); }
  .l10 { color: var(--c10); }
  .l11 { color: var(--c11); }
  .l12 { color: var(--c12); }
  .l13 { color: var(--c13); }
</style>
</head>
<body>
<main class="cover">
  <div class="cover__scenery" role="img" aria-label="Autumn trees in yellow and orange reflected in a still lake, with a pale scratched texture over it"></div>

  <svg class="cover__heart" width="1200" height="1200" viewBox="0 0 1200 1200" aria-hidden="true">
    <defs>
      <linearGradient id="heart-tide" x1="0" y1="228" x2="0" y2="975" gradientUnits="userSpaceOnUse">
        <stop offset="0" stop-color="var(--heart-top)"/>
        <stop offset="0.5" stop-color="var(--heart-mid)"/>
        <stop offset="1" stop-color="var(--heart-low)"/>
      </linearGradient>
    </defs>
    <path class="heart-outline" fill="none" stroke="url(#heart-tide)" stroke-width="32" stroke-linejoin="miter" stroke-miterlimit="12"
      d="M600,395 C560,300 470,244 380,244 C272,244 214,330 220,432 C228,560 330,660 420,760 L600,955 L780,760 C870,660 972,560 980,432 C986,330 928,244 820,244 C730,244 640,300 600,395 Z"/>
  </svg>

  <h1 class="cover__title" aria-label="Quiet Harbours"><span class="l1">Q</span><span class="l2">U</span><span class="l3">I</span><span class="l4">E</span><span class="l5">T</span> <span class="l6">H</span><span class="l7">A</span><span class="l8">R</span><span class="l9">B</span><span class="l10">O</span><span class="l11">U</span><span class="l12">R</span><span class="l13">S</span></h1>
</main>
</body>
</html>
```